New business Cards

We need some new cards that stand out. We love our logo and colour scheme but need to incorporate a numo logo and ptl logo yet still keep our cards uncluttered and clean looking.
Our tag is Keen Ledgerworks. Anywhere, Anytime.
The idea of the cards is to show authority in accounting and Numo/ cloud software

```html
<!DOCTYPE html>
<html lang="en">
<head>
<meta charset="utf-8">
<title>Marlow Business Solutions – Business Cards</title>
<link rel="stylesheet" href="https://fonts.googleapis.com/css2?family=Open+Sans:wght@600;700&family=Arimo:wght@400;700&family=Tinos&display=swap">
<style>
  :root {
    --backdrop: #e9ecee;
    --brand-green: #6dbe45;
    --slit-dark: #1d2a12;
    --ink: #2a2a2a;
    --white: #ffffff;
    --paper-grey: #d9d9d9;
    --accent-orange: #f07a22;
    --accent-peach: #f6b77a;
    --blue-light: #1ea6e2;
    --blue-deep: #1f49a6;
    --name-yellow: #ffe600;
    --badge-gold: #f3c019;
  }
  * { box-sizing: border-box; margin: 0; padding: 0; }
  html, body { width: 1200px; height: 900px; overflow: hidden; }
  body { background: var(--backdrop); position: relative; }

  .card {
    position: absolute;
    left: 250px;
    width: 700px;
    height: 400px;
    overflow: hidden;
    box-shadow: 0 6px 18px rgba(0,0,0,.18);
  }

  /* Front card */
  .card-front { top: 40px; background: var(--brand-green); }
  .slit {
    position: absolute;
    left: 50px;
    width: 600px;
    height: 26px;
    border-radius: 50%;
    background: radial-gradient(ellipse at center, rgba(29,42,18,.85) 0%, rgba(29,42,18,.35) 55%, rgba(29,42,18,0) 72%);
  }
  .slit-top { top: 70px; }
  .slit-bottom { top: 238px; }
  .front-brand {
    position: absolute;
    top: 130px;
    left: 40px;
    display: flex;
    align-items: center;
    gap: 22px;
  }
  .brand-mark {
    width: 86px;
    height: 86px;
    background: var(--white);
  }
  .brand-name {
    font-family: "Open Sans", sans-serif;
    font-weight: 700;
    font-size: 40px;
    color: var(--white);
    letter-spacing: -0.5px;
  }
  .front-tagline {
    position: absolute;
    bottom: 34px;
    left: 48px;
    font-family: "Tinos", serif;
    font-size: 36px;
    color: var(--ink);
    letter-spacing: 0.5px;
  }

  /* Back card */
  .card-back { top: 470px; }
  .back-art { position: absolute; inset: 0; }
  .back-brand {
    position: absolute;
    top: 26px;
    right: 34px;
    display: flex;
    align-items: center;
    gap: 12px;
  }
  .back-brand .brand-mark { width: 44px; height: 44px; background: var(--brand-green); }
  .back-brand .brand-name { font-size: 24px; color: var(--brand-green); }

  .holder {
    position: absolute;
    top: 206px;
    left: 42px;
    font-family: "Arimo", sans-serif;
  }
  .holder-name {
    font-weight: 700;
    font-size: 32px;
    color: var(--name-yellow);
  }
  .holder-name .post-nominals {
    font-weight: 400;
    font-size: 20px;
    margin-left: 4px;
  }
  .holder-role {
    font-weight: 700;
    font-size: 24px;
    color: var(--white);
    margin-top: 2px;
  }
  .partner-badges {
    position: absolute;
    left: 24px;
    bottom: 28px;
    display: flex;
    gap: 6px;
  }
  .badge {
    width: 130px;
    height: 44px;
    background: var(--white);
    border: 2px solid var(--white);
  }
  .badge-software { display: flex; align-items: center; gap: 8px; padding-left: 10px; }
  .badge-software span { width: 30px; height: 30px; border-radius: 50%; background: var(--blue-light); }
  .badge-body { background: var(--blue-deep); display: flex; justify-content: flex-end; }
  .badge-body span { width: 34px; height: 100%; background: var(--badge-gold); }

  .contact {
    position: absolute;
    right: 36px;
    top: 250px;
    text-align: right;
    font-family: "Tinos", serif;
    font-size: 23px;
    line-height: 1.18;
    color: var(--white);
    list-style: none;
  }
</style>
</head>
<body>

<section class="card card-front" aria-label="Business card front">
  <div class="slit slit-top"></div>
  <div class="front-brand">
    <div class="brand-mark"></div>
    <h1 class="brand-name">Marlow Business Solutions</h1>
  </div>
  <p class="front-tagline">keen ledgerworks. anywhere, anytime.</p>
  <div class="slit slit-bottom"></div>
</section>

<section class="card card-back" aria-label="Business card back">
  <svg class="back-art" width="700" height="400" viewBox="0 0 700 400" aria-hidden="true">
    <defs>
      <linearGradient id="paper" x1="0" y1="0" x2="0" y2="1">
        <stop offset="0" stop-color="#f4f4f4"/>
        <stop offset="1" stop-color="#d4d4d4"/>
      </linearGradient>
      <linearGradient id="band" x1="0" y1="0" x2="1" y2="0">
        <stop offset="0" stop-color="#f8d3a8"/>
        <stop offset="1" stop-color="#f07a22"/>
      </linearGradient>
      <linearGradient id="sea" x1="0" y1="0" x2="0" y2="1">
        <stop offset="0" stop-color="#1ea6e2"/>
        <stop offset="1" stop-color="#1f49a6"/>
      </linearGradient>
    </defs>
    <rect width="700" height="400" fill="url(#paper)"/>
    <path d="M0 180 C 180 140, 420 120, 700 118 L700 400 L0 400 Z" fill="url(#band)"/>
    <path d="M0 196 C 200 160, 440 150, 700 152 L700 400 L0 400 Z" fill="url(#sea)"/>
  </svg>

  <div class="back-brand">
    <div class="brand-mark"></div>
    <span class="brand-name">Marlow Business Solutions</span>
  </div>

  <div class="holder">
    <h2 class="holder-name">Eleanor Marlow,<span class="post-nominals">PTL, KLA</span></h2>
    <p class="holder-role">Partner</p>
  </div>

  <div class="partner-badges">
    <div class="badge badge-software" role="img" aria-label="Numo partner badge"><span></span><span></span></div>
    <div class="badge badge-body" role="img" aria-label="PTL member badge"><span></span></div>
  </div>

  <ul class="contact">
    <li>Ashby Vic 3999</li>
    <li>p: 03 5550 0142</li>
    <li>e: eleanorm@marlowbizsol.com.au</li>
    <li>www.marlowbizsol.com.au</li>
  </ul>
</section>

</body>
</html>
```